Location services company card

Design a new business card for our location services company. I would like to have the front fairly standard with phone and email, logo, name, title etc. Back should feature text: "Location intelligence: make better decisions with maps." I would like either a location pin on the back to make it obvious that we are involved with maps. This could also have a small mud map on the back (use Vensu.com for design inspiration here).

Target Market(s)

Business and government

Industry/Entity Type

Consultant

Contact Information for Business Card

Name, title, address, phone, mobile, email

Font styles to use
Sans Serif

Requirements
Must have
• Flat design with the company colours:
• C60 M0 Y100 K0 and C100 M20 Y0 K65
• Location pin and/or mud map on back.
• Design must be similar/consistent in feel to tqav.com.au

```html
<!DOCTYPE html>
<html lang="en">
<head>
<meta charset="utf-8">
<title>TQAV Business Card</title>
<link rel="stylesheet" href="https://fonts.googleapis.com/css2?family=Arimo:wght@400;700&display=swap">
<style>
  :root {
    --green: #69b636;
    --green-dark: #4f8f27;
    --navy: #1c3d5c;
    --white: #ffffff;
    --stage: #2b2b2b;
    --ink-light: #e9eef3;
    --ink-dark: #10202e;
  }
  * { margin: 0; padding: 0; box-sizing: border-box; }
  html, body {
    width: 1200px; height: 997px; overflow: hidden;
    background: var(--stage);
    font-family: "Arimo", Arial, sans-serif;
  }
  .canvas { position: relative; width: 1200px; height: 997px; }

  .card {
    position: absolute; width: 560px; height: 320px;
    border-radius: 22px; overflow: hidden;
    background: var(--white);
  }
  .card-back { left: 90px; top: 100px; }
  .card-front { left: 550px; top: 480px; }

  .brand-name {
    position: absolute; left: 0; width: 100%; text-align: center;
    color: var(--navy); font-weight: 700; letter-spacing: 1px; line-height: 1;
  }

  .card-back .brand-name { top: 44px; font-size: 54px; }
  .pin-mark { position: absolute; left: 250px; top: 124px; width: 60px; height: 82px; }
  .back-statement {
    position: absolute; left: 0; bottom: 44px; width: 100%; text-align: center;
    color: var(--navy); font-size: 14px; letter-spacing: 0.4px;
    text-transform: uppercase; white-space: nowrap;
  }

  .front-bands { position: absolute; inset: 0; width: 560px; height: 320px; }
  .card-front .brand-name { top: 40px; font-size: 50px; }
  .person {
    position: absolute; left: 185px; top: 130px; width: 200px; text-align: center;
  }
  .person-name { color: var(--white); font-weight: 700; font-size: 17px; letter-spacing: 0.5px; line-height: 20px; }
  .person-title { color: var(--ink-dark); font-size: 14px; line-height: 16px; margin-top: 1px; }
  .website {
    position: absolute; right: 30px; top: 204px;
    color: var(--green); font-size: 16px;
  }
  .contact-list { position: absolute; left: 28px; top: 222px; list-style: none; }
  .contact-list li {
    display: flex; align-items: flex-start; gap: 12px;
    color: var(--ink-light); font-size: 15px; line-height: 18px; margin-bottom: 6px;
  }
  .contact-icon { flex: none; width: 18px; height: 18px; }
</style>
</head>
<body>
<main class="canvas">

  <section class="card card-back" aria-label="Card back">
    <div class="brand-name">tqav</div>
    <svg class="pin-mark" viewBox="0 0 60 82" aria-label="Location pin">
      <path d="M30 2C14 2 2 14 2 30c0 20 28 50 28 50s28-30 28-50C58 14 46 2 30 2z" fill="var(--green)"/>
      <circle cx="30" cy="29" r="11" fill="var(--white)"/>
    </svg>
    <p class="back-statement">Location intelligence: make better decisions with maps</p>
  </section>

  <section class="card card-front" aria-label="Card front">
    <svg class="front-bands" viewBox="0 0 560 320" aria-hidden="true">
      <path d="M0 196 L560 150 L560 320 L0 320 Z" fill="var(--navy)"/>
      <path d="M150 184 L138 178 L162 183 Z" fill="var(--green-dark)"/>
      <path d="M420 162 L436 150 L408 163 Z" fill="var(--green-dark)"/>
      <path d="M150 184 L178 124 L392 124 L420 162 Z" fill="var(--green)"/>
      <path d="M0 196 L560 150" stroke="var(--green)" stroke-width="5"/>
    </svg>
    <div class="brand-name">tqav</div>
    <div class="person">
      <div class="person-name">MATEO RIVAS</div>
      <div class="person-title">Managing Director</div>
    </div>
    <div class="website">www.tqav.com.au</div>
    <ul class="contact-list">
      <li>
        <svg class="contact-icon" viewBox="0 0 18 18" aria-label="Phone"><circle cx="9" cy="9" r="9" fill="var(--green)"/><path d="M5 7c0-1 1-2 4-2s4 1 4 2l-1.5 1L10 7H8L6.5 8z M6 9h6v4H6z" fill="var(--navy)"/></svg>
        <span>+61 400555123</span>
      </li>
      <li>
        <svg class="contact-icon" viewBox="0 0 18 18" aria-label="Email"><circle cx="9" cy="9" r="9" fill="var(--green)"/><rect x="4.5" y="6" width="9" height="6" fill="var(--navy)"/><path d="M4.5 6L9 9.5L13.5 6" stroke="var(--green)" fill="none"/></svg>
        <span>info@tqav.com.au</span>
      </li>
      <li>
        <svg class="contact-icon" viewBox="0 0 18 18" aria-label="Address"><circle cx="9" cy="9" r="9" fill="var(--green)"/><path d="M9 4a3.2 3.2 0 0 0-3.2 3.2C5.8 10 9 14 9 14s3.2-4 3.2-6.8A3.2 3.2 0 0 0 9 4z" fill="var(--navy)"/></svg>
        <span>4b/27 Harlow Street,<br>Kelmore WA 6200, Australia</span>
      </li>
    </ul>
  </section>

</main>
</body>
</html>
```